BrimFalcon Business Cards

We have a defined brand. Please visit our website to get a feel for the product and the color pallets. www.brimfalcon-demo.com

We need an updated, world class business card design. (See the attached existing card design). Please utilize BOTH sides of the card as shown and be creative with the layout. I do want the horse head icon to be positioned as it is with the existing card.

The remainder of the layout can be customized and I also want it vertically oriented.

Attached are the logo files and please use the colors as follows:
Green - #A5CE39
Tan - #CDBD99
Black

Feel free to play with the colors.

```html
<!DOCTYPE html>
<html lang="en">
<head>
<meta charset="utf-8">
<title>BrimFalcon – Business Cards</title>
<link href="https://fonts.googleapis.com/css2?family=Roboto+Slab:wght@400;700&display=swap" rel="stylesheet">
<style>
  :root {
    --brand-green: #A5CE39;
    --brand-black: #111111;
    --card-white: #ffffff;
    --backdrop: #2b2e33;
  }
  * { margin: 0; padding: 0; box-sizing: border-box; }
  html, body { width: 1200px; height: 900px; overflow: hidden; }
  body {
    background: var(--backdrop);
    position: relative;
    font-family: "Roboto Slab", serif;
    color: var(--brand-black);
  }
  .card {
    position: absolute;
    top: 150px;
    width: 360px;
    height: 600px;
    overflow: hidden;
    background: var(--brand-green);
  }
  .card--front { left: 150px; }
  .card--back { left: 690px; }

  /* Front */
  .mark-area {
    position: absolute;
    left: 50px; top: 70px;
    width: 260px; height: 260px;
    border-radius: 50%;
    background: var(--brand-black);
  }
  .wordmark {
    font-family: "Roboto Slab", serif;
    font-weight: 700;
    color: var(--brand-black);
    white-space: nowrap;
  }
  .card--front .wordmark {
    position: absolute;
    left: 0; right: 0; top: 392px;
    text-align: center;
    font-size: 44px;
    line-height: 1;
  }
  .tagline {
    position: absolute;
    left: 0; right: 0; top: 452px;
    text-align: center;
    font-size: 16px;
    font-weight: 400;
    letter-spacing: 2px;
    white-space: nowrap;
  }

  /* Back */
  .back-split { position: absolute; inset: 0; }
  .name-badge {
    position: absolute;
    left: 40px; top: 44px;
    width: 280px; height: 84px;
    border-radius: 10px;
    background: var(--brand-green);
    text-align: center;
    padding-top: 14px;
  }
  .name-badge__name { font-weight: 700; font-size: 24px; letter-spacing: 1px; line-height: 1.2; }
  .name-badge__title { font-size: 17px; margin-top: 2px; }
  .card--back .brand-line {
    position: absolute;
    left: 40px; top: 158px;
    display: flex; align-items: center; gap: 12px;
  }
  .brand-dot {
    width: 26px; height: 26px;
    border-radius: 50%;
    background: var(--brand-black);
    flex: none;
  }
  .card--back .wordmark { font-size: 32px; line-height: 1; }
  .contact-list {
    position: absolute;
    left: 36px; top: 360px;
    list-style: none;
  }
  .contact-list li {
    display: flex; align-items: center; gap: 14px;
    height: 46px;
    font-size: 15px;
    white-space: nowrap;
  }
  .contact-icon {
    width: 30px; height: 30px;
    border: 2px solid var(--brand-black);
    border-radius: 8px;
    display: flex; align-items: center; justify-content: center;
    flex: none;
  }
  .contact-list .address { line-height: 1.25; }
</style>
</head>
<body>

<section class="card card--front">
  <div class="mark-area" role="img" aria-label="Brand symbol area"></div>
  <div class="wordmark">BrimFalcon</div>
  <div class="tagline">Electric Motion, Built Bold</div>
</section>

<section class="card card--back">
  <svg class="back-split" width="360" height="600" viewBox="0 0 360 600" aria-hidden="true">
    <polygon points="0,0 360,0 360,200 0,340" fill="var(--card-white)"/>
    <line x1="0" y1="352" x2="360" y2="212" stroke="var(--card-white)" stroke-width="3"/>
  </svg>
  <div class="name-badge">
    <div class="name-badge__name">JORDAN REYES</div>
    <div class="name-badge__title">President &amp; CEO</div>
  </div>
  <div class="brand-line">
    <span class="brand-dot"></span>
    <span class="wordmark">BrimFalcon</span>
  </div>
  <ul class="contact-list">
    <li>
      <span class="contact-icon">
        <svg width="16" height="16" viewBox="0 0 16 16"><path d="M3 1l3 3-2 2c1 2 3 4 5 5l2-2 3 3-2 3C7 15 1 9 1 3z" fill="var(--brand-black)"/></svg>
      </span>
      306 555 0148
    </li>
    <li>
      <span class="contact-icon">
        <svg width="16" height="14" viewBox="0 0 16 14"><rect x="1" y="2" width="14" height="10" fill="none" stroke="var(--brand-black)" stroke-width="1.6"/><path d="M1 2l7 6 7-6" fill="none" stroke="var(--brand-black)" stroke-width="1.6"/></svg>
      </span>
      jordan@brimfalcon-demo.com
    </li>
    <li>
      <span class="contact-icon">
        <svg width="16" height="16" viewBox="0 0 16 16" fill="none" stroke="var(--brand-black)" stroke-width="1.4"><circle cx="8" cy="8" r="6.5"/><ellipse cx="8" cy="8" rx="3" ry="6.5"/><line x1="1.5" y1="8" x2="14.5" y2="8"/></svg>
      </span>
      brimfalcon-studio-demo.com
    </li>
    <li>
      <span class="contact-icon">
        <svg width="14" height="16" viewBox="0 0 14 16"><path d="M7 1a5 5 0 0 1 5 5c0 4-5 9-5 9S2 10 2 6a5 5 0 0 1 5-5z" fill="var(--brand-black)"/><circle cx="7" cy="6" r="2" fill="var(--brand-green)"/></svg>
      </span>
      <span class="address">Northvale, Saskatchewan<br>canada</span>
    </li>
  </ul>
</section>

</body>
</html>
```